The Wellness Barn Business Card

Info for the front..... (in whichever order and layout looks best)
Carla Penhallow
Physiotherapist
4/37 Upper Creekbank Rd
Tallowbrook
QLD 4712
0462305178
carlapenhallow57@mailbox.example
www.thewellnessbarn.example.au
on the back I would like to be able to write appointments so probably just that heading with lines.
I like a sort of rustic style but mostly professional, colours in naturals, beige, brown, green etc. I dont mind if the logo colour is changed slightly to suit.

```html
<!DOCTYPE html>
<html lang="en">
<head>
<meta charset="utf-8">
<title>The Wellness Barn Business Card</title>
<link href="https://fonts.googleapis.com/css2?family=Cinzel:wght@400;600&family=Lato:wght@400;700;900&display=swap" rel="stylesheet">
<style>
  :root {
    --stage: #222222;
    --clay: #a57a5c;
    --sand: #d2c69c;
    --sand-light: #dccfa4;
    --forest: #2d4a22;
  }
  * { margin: 0; padding: 0; box-sizing: border-box; }
  html, body { width: 1200px; height: 1000px; overflow: hidden; }
  body { background: var(--stage); position: relative; font-family: "Lato", sans-serif; }

  .card {
    position: absolute;
    left: 201px;
    width: 798px;
    height: 456px;
    border-radius: 18px;
    box-shadow: 0 6px 24px rgba(0,0,0,0.45);
  }
  .card--back { top: 33px; background: var(--clay); }
  .card--front { top: 510px; background: var(--sand); color: var(--forest); }

  .brand-name {
    position: absolute;
    font-family: "Lato", sans-serif;
    font-weight: 900;
    text-align: center;
    line-height: 1.02;
  }
  .card--back .brand-name {
    left: 0; right: 0; top: 95px;
    color: var(--sand-light);
    font-size: 66px;
  }
  .card--front .brand-name {
    left: 480px; width: 300px; top: 40px;
    color: var(--forest);
    font-size: 56px;
  }

  .appointments {
    position: absolute;
    left: 255px; top: 380px;
    width: 289px; height: 36px;
    border-top: 1px solid rgba(220,207,164,0.7);
    border-bottom: 1px solid rgba(220,207,164,0.7);
    display: flex; align-items: center;
    color: var(--sand-light);
  }
  .appointments__icon { width: 44px; display: flex; justify-content: center; }
  .appointments__divider { width: 1px; height: 36px; background: rgba(220,207,164,0.7); }
  .appointments__label {
    font-family: "Cinzel", serif;
    font-size: 24px;
    letter-spacing: 0.5px;
    padding-left: 6px;
  }

  .person { position: absolute; left: 27px; top: 24px; }
  .person__name {
    font-family: "Cinzel", serif;
    font-weight: 600;
    font-size: 34px;
    line-height: 1.1;
  }
  .person__role {
    font-weight: 900;
    font-size: 22px;
    letter-spacing: 0.8px;
    margin-top: 4px;
  }

  .contact-list {
    position: absolute;
    left: 27px; top: 336px;
    list-style: none;
    font-size: 20px;
    color: #1f2a18;
  }
  .contact-list li { display: flex; align-items: center; height: 28.5px; }
  .contact-list svg { width: 15px; height: 15px; margin-right: 8px; fill: var(--forest); }

  .address {
    position: absolute;
    left: 463px; top: 364px;
    display: flex;
    font-size: 20px;
    color: #1f2a18;
    line-height: 28.5px;
  }
  .address svg { width: 16px; height: 18px; margin: 5px 2px 0 0; fill: var(--forest); }
</style>
</head>
<body>

<section class="card card--back">
  <div class="brand-name">The<br>Wellness<br>Barn</div>
  <div class="appointments">
    <span class="appointments__icon">
      <svg width="22" height="24" viewBox="0 0 22 24" fill="none" stroke="#dccfa4" stroke-width="1.5">
        <rect x="2" y="4" width="16" height="18" rx="2"/>
        <line x1="6" y1="2" x2="6" y2="6"/><line x1="14" y1="2" x2="14" y2="6"/>
        <line x1="5" y1="10" x2="11" y2="10"/><line x1="5" y1="14" x2="9" y2="14"/>
        <circle cx="15" cy="17" r="3"/>
      </svg>
    </span>
    <span class="appointments__divider"></span>
    <span class="appointments__label">APPOINTMENTS</span>
  </div>
</section>

<section class="card card--front">
  <div class="person">
    <div class="person__name">Carla Penhallow</div>
    <div class="person__role">PHYSIOTHERAPIST</div>
  </div>

  <div class="brand-name">The<br>Wellness<br>Barn</div>

  <ul class="contact-list">
    <li>
      <svg viewBox="0 0 24 24"><path d="M6.6 10.8a15 15 0 0 0 6.6 6.6l2.2-2.2a1 1 0 0 1 1-.25 11.4 11.4 0 0 0 3.6.57 1 1 0 0 1 1 1V20a1 1 0 0 1-1 1A17 17 0 0 1 3 4a1 1 0 0 1 1-1h3.5a1 1 0 0 1 1 1c0 1.25.2 2.45.57 3.57a1 1 0 0 1-.25 1z"/></svg>
      0462305178
    </li>
    <li>
      <svg viewBox="0 0 24 24"><path d="M2 11 22 3l-8 19-3-8z"/></svg>
      carlapenhallow57@mailbox.example
    </li>
    <li>
      <svg viewBox="0 0 24 24"><path d="M12 2a10 10 0 1 0 0 20 10 10 0 0 0 0-20zm6.9 6h-3a15 15 0 0 0-1.3-3.9A8 8 0 0 1 18.9 8zM12 4c.9 1.2 1.6 2.5 2 4h-4c.4-1.5 1.1-2.8 2-4zM4.3 14a8 8 0 0 1 0-4h3.4a16 16 0 0 0 0 4zm.8 2h3a15 15 0 0 0 1.3 3.9A8 8 0 0 1 5.1 16zm3-8h-3a8 8 0 0 1 4.3-3.9C8.8 5.3 8.4 6.6 8.1 8zM12 20c-.9-1.2-1.6-2.5-2-4h4c-.4 1.5-1.1 2.8-2 4zm2.3-6H9.7a14 14 0 0 1 0-4h4.6a14 14 0 0 1 0 4zm.3 5.9c.6-1.2 1-2.5 1.3-3.9h3a8 8 0 0 1-4.3 3.9zm1.7-5.9a16 16 0 0 0 0-4h3.4a8 8 0 0 1 0 4z"/></svg>
      www.thewellnessbarn.example.au
    </li>
  </ul>

  <div class="address">
    <svg viewBox="0 0 24 28"><path d="M12 1a9 9 0 0 0-9 9c0 7 9 17 9 17s9-10 9-17a9 9 0 0 0-9-9zm0 12.5A3.5 3.5 0 1 1 12 6.5a3.5 3.5 0 0 1 0 7z"/></svg>
    <div>4/37 Upper Creekbank Rd<br>Tallowbrook, QLD 4712</div>
  </div>
</section>

</body>
</html>
```